Website for business consultancy - bright and happy feel needed

I need a website with 3/4 pages. I want the first page designed first and the rest will be easy. I need some pictures but none with corporate looking people. I need links to quillpost and deskroster. I need a contact form. I have samples of websites i like, fonts i like and I need a small logo also. I like simple, clean lines and I want a bright, happy and feminine feel. My audience are small businesses so I don't want them intimidated by new much of a corporate feel.
Updates

Target Market(s)

Small medium size businesses who want to grow and need that help but they cannot afford a full time financial director.

Industry/Entity Type

Business Consultant

Number of Pages Required

4 page

Other font styles liked:
• i can attach images

Colors
fcf0f6
e667a6
85cae6
ffffff
fbee3e

Requirements
Must have
• Link to quillpost and desk roster
• Contact form linked to my email
• Pictures - full width images where required
• Colour
• Mobile ready
• Soft feminine feel to it
• I dont want it to look like a corporate business consultancy - much more marketing or interior deign feel
Nice to have
• I would like the 3 services I have in 3 boxes that you click and takes you to a place with more information on the service.
• pictures thinking outside of the box
• Can be wordpress if need be
Should not have
• pictures with too much of a corporate feel
• No pictures of coporate people at all
• i like the following websites
• www.marbelquint.co.uk and others that are attached in the documents with a feminine feel to them

```html
<!DOCTYPE html>
<html lang="en">
<head>
<meta charset="utf-8">
<title>Maren Holt Consultancy</title>
<link href="https://fonts.googleapis.com/css2?family=Open+Sans:ital,wght@0,400;0,600;0,700;1,400;1,700&display=swap" rel="stylesheet">
<style>
:root{
  --pink:#e667a6;
  --pink-deep:#d63f8a;
  --pink-soft:#fcf0f6;
  --blue:#85cae6;
  --blue-line:#6cc0e3;
  --white:#ffffff;
  --ink:#333333;
  --grey:#888888;
  --light:#f1f1f1;
  --rule:#e3e3e3;
  --dark:#3a3a3a;
  --darker:#2b2b2b;
  --field:#5a5a5a;
}
*{box-sizing:border-box;margin:0;padding:0}
html,body{width:1200px;height:3191px;overflow:hidden}
body{font-family:"Open Sans",Arial,sans-serif;color:var(--ink);background:var(--white);position:relative}
a{color:inherit;text-decoration:none}

.topbar{height:36px;background:var(--dark);color:#bdbdbd;font-size:13px;display:flex;align-items:center;padding-left:82px;gap:34px}
.topbar span{display:flex;align-items:center;gap:8px}
.topbar svg{width:12px;height:12px;fill:#bdbdbd}

.masthead{height:124px;display:flex;align-items:center;justify-content:center;gap:14px;border-bottom:2px solid var(--blue)}
.brand-dot{width:48px;height:48px;border-radius:50%;background:var(--blue)}
.brand-name{font-size:28px;font-weight:400;color:var(--pink);line-height:1}
.brand-name small{display:block;font-size:17px;margin-top:6px}

.mainnav{height:53px;display:flex;align-items:center;padding-left:117px;gap:56px;font-size:13px;text-transform:uppercase;border-bottom:1px solid var(--rule)}
.mainnav a.current{color:var(--pink);position:relative}
.mainnav a.current::before{content:"";position:absolute;left:-10px;right:-10px;top:-18px;height:3px;background:var(--pink)}

.hero{position:relative;height:479px;overflow:hidden;background:linear-gradient(120deg,#f07bb4,#d9529b 55%,#c63e8e)}
.hero-photo{position:absolute;inset:0;background:linear-gradient(180deg,#cfe7f4,#8fb5cf 70%,#6f8ea6);clip-path:polygon(0 0,485px 0,325px 100%,0 100%)}
.hero-edge{position:absolute;inset:0;background:var(--blue);clip-path:polygon(485px 0,491px 0,331px 100%,325px 100%)}
.hero-copy{position:absolute;left:596px;top:150px;color:var(--white)}
.hero-copy h1{font-size:25px;font-weight:400;margin-bottom:16px}
.hero-copy p{font-size:16px;line-height:22px;width:480px}
.btn-outline{display:inline-block;margin-top:22px;border:2px solid var(--white);padding:7px 20px;font-size:12px;text-transform:uppercase}
.slider-dots{position:absolute;left:608px;top:600px;display:flex;gap:8px;align-items:center}
.slider-dots i{width:14px;height:14px;border-radius:50%;background:var(--blue)}
.slider-dots i.on{width:22px;height:22px;background:var(--white)}

.welcome{height:266px;background:var(--light);position:relative}
.welcome-photo{position:absolute;left:98px;top:50px;width:178px;height:176px;border:2px solid #c9c9c9;border-radius:10px;background:linear-gradient(135deg,#f2d9c4,#b88b6e 60%,#5d4a43)}
.welcome h2{position:absolute;left:306px;top:70px;font-size:27px;font-weight:400}
.welcome p{position:absolute;left:306px;top:114px;width:630px;font-size:15px;line-height:21px;color:#555}
.welcome .slider-dots{left:1003px;top:120px}
.welcome .slider-dots i.on{background:var(--pink)}

.content{position:absolute;left:81px;top:1000px;width:1032px}
.section-title{font-size:26px;font-weight:400;text-transform:uppercase;padding-bottom:14px;position:relative;margin-top:28px}
.section-title::after{content:"";position:absolute;left:0;bottom:0;width:88px;height:3px;background:var(--pink)}
.posts{position:absolute;left:0;top:107px;width:645px}
.post{height:254px;position:relative;border-bottom:2px solid var(--rule);margin-bottom:0}
.post+.post{margin-top:0}
.post-photo{position:absolute;left:0;top:0;width:189px;height:187px}
.post h3{position:absolute;left:223px;top:14px;font-size:19px;font-weight:400}
.post p{position:absolute;left:223px;top:50px;width:420px;font-size:14.5px;line-height:20.5px;color:var(--grey)}
.btn-pink{position:absolute;left:238px;top:153px;background:var(--pink);color:var(--white);font-size:11px;font-weight:600;padding:4px 14px}
.post time{position:absolute;right:4px;top:156px;font-size:11px;font-style:italic;color:#aaa}
.view-more{position:absolute;left:555px;top:1000px;background:#555;color:var(--white);font-size:11px;padding:6px 20px}
.post-divider{position:absolute;left:702px;top:40px;width:1px;height:1100px;background:var(--rule)}

.sidebar{position:absolute;left:762px;top:32px;width:270px}
.search{display:flex;height:36px}
.search span{flex:1;background:#f3f3f3;border:1px solid var(--rule)}
.search b{width:73px;background:var(--pink);color:var(--white);font-size:12px;font-weight:400;display:flex;align-items:center;justify-content:center}
.widget{border-bottom:2px solid var(--rule);padding:28px 0 24px}
.widget h4{font-size:19px;font-weight:400;margin-bottom:12px}
.widget p{font-size:14px;line-height:19px;color:#555}
.field{height:34px;background:#f3f3f3;margin-top:18px;font-size:11px;color:#aaa;padding:9px 18px}
.btn-blue{display:inline-block;margin-top:12px;background:var(--blue);color:var(--white);font-size:11px;padding:8px 14px}
.connect{display:flex;gap:18px}
.connect span{flex:1;height:28px;background:var(--blue-line);color:var(--white);font-size:10px;display:flex;align-items:center;gap:8px;padding-left:6px}
.connect span:first-child{background:#3b5a98}
.connect i{width:16px;height:16px;background:var(--white);opacity:.85}
.tw-profile{position:relative;height:150px;background:#f7f7f7}
.tw-avatar{position:absolute;left:0;top:0;width:88px;height:88px;background:linear-gradient(135deg,#bfd3e6,#8aa0b8)}
.tw-profile strong{position:absolute;left:102px;top:2px;font-size:14px;font-weight:400}
.tw-profile em{position:absolute;left:102px;top:20px;font-size:11px;color:#999;font-style:normal}
.tw-profile small{position:absolute;left:102px;top:40px;width:165px;font-size:9px;line-height:11px;color:#555}
.tw-follow{position:absolute;left:22px;top:108px;background:var(--white);border:1px solid var(--rule);font-size:9px;padding:3px 10px}
.tweet{position:relative;height:135px;border-bottom:2px solid var(--rule)}
.tweet-avatar{position:absolute;left:0;top:18px;width:40px;height:40px;background:linear-gradient(135deg,#bfd3e6,#8aa0b8)}
.tweet strong{position:absolute;left:52px;top:20px;font-size:12px;font-weight:400}
.tweet em{position:absolute;left:52px;top:36px;font-size:10px;color:#999;font-style:normal}
.tweet p{position:absolute;left:0;top:64px;font-size:10px;line-height:13px;color:#555}
.tweet p b{color:var(--blue-line);font-weight:400}
.tweet time{position:absolute;right:10px;top:100px;font-size:9px;color:#aaa}
.tw-foot{display:flex;justify-content:space-between;font-size:10px;color:var(--blue-line);padding:10px 18px 0}

.cards{position:absolute;left:81px;top:2234px;display:flex;gap:12px}
.card{width:249px;height:388px;background:var(--white);box-shadow:0 0 4px rgba(0,0,0,.15);border-top:3px solid var(--blue);position:relative;text-align:center}
.card-photo{height:184px}
.card h5{font-size:14px;font-weight:400;margin-top:24px}
.card h5::after{content:"";display:block;width:96px;height:1px;background:#ccc;margin:14px auto 0}
.card p{font-size:12px;line-height:16px;color:#555;width:190px;margin:14px auto 0}
.card a{position:absolute;left:0;right:0;bottom:0;height:34px;background:var(--blue);color:var(--white);font-size:12px;line-height:34px}
.card.active{background:var(--pink);border-top-color:var(--pink)}
.card.active h5,.card.active p{color:var(--white)}
.card.active h5::after{background:rgba(255,255,255,.7)}
.card.active a{background:var(--pink-deep)}

.footer{position:absolute;left:0;top:2734px;width:1200px;height:384px;background:var(--dark);color:var(--white)}
.footer h6{font-size:20px;font-weight:400;margin-bottom:34px}
.fcol{position:absolute;top:70px}
.fcol ul{list-style:none;font-size:16px;line-height:28px}
.fcol .who{font-size:19px;font-weight:700;font-style:italic;margin-bottom:4px}
.fcol .lines{font-size:16px;line-height:28px}
.fcol .intro{font-size:14px;line-height:19px;width:218px}
.ffield{width:215px;height:32px;background:var(--field);margin-top:12px;font-size:10px;color:#ccc;padding:8px 14px}
.ffield.tall{height:72px;margin-top:6px}
.fsend{position:absolute;left:123px;top:310px;background:var(--pink-deep);font-size:11px;padding:6px 28px}
.socials{display:flex;gap:14px}
.socials span{width:42px;height:42px;border:2px solid var(--white);border-radius:50%;display:flex;align-items:center;justify-content:center;font-size:8px;text-align:center}
.copyright{position:absolute;left:0;top:3118px;width:1200px;height:73px;background:var(--darker);color:var(--white);font-size:17px;padding:25px 0 0 96px}
</style>
</head>
<body>

<div class="topbar">
  <span><svg viewBox="0 0 12 12"><path d="M2 1l2-1 2 3-1.5 1.5a6 6 0 003 3L9 6l3 2-1 2c-5 1-10-4-9-9z"/></svg>(010) 555 0192</span>
  <span><svg viewBox="0 0 12 12"><path d="M6 0a4 4 0 014 4c0 3-4 8-4 8S2 7 2 4a4 4 0 014-4zm0 2.5a1.5 1.5 0 100 3 1.5 1.5 0 000-3z"/></svg>42 Willowbank Lane Ashford, CT 06000</span>
  <span><svg viewBox="0 0 12 12"><path d="M0 2h12v8H0zM1 3l5 4 5-4"/></svg>info@marenholt.com</span>
</div>

<header class="masthead">
  <span class="brand-dot"></span>
  <div class="brand-name">Maren Holt<small>Consultancy</small></div>
</header>

<nav class="mainnav">
  <a href="#">Home</a><a href="#" class="current">Blog</a><a href="#">Services</a><a href="#">News</a><a href="#">Contact</a>
</nav>

<section class="hero">
  <div class="hero-photo" role="img" aria-label="City skyline of bright office towers under a pale sky"></div>
  <div class="hero-edge"></div>
  <div class="hero-copy">
    <h1>Lorem Ipsum is simply dummy text</h1>
    <p>There are many variations of passages of Lorem Ipsum available, which don't look even slightly believable.</p>
    <a href="#" class="btn-outline">Read More</a>
  </div>
  <div class="slider-dots"><i class="on"></i><i></i><i></i></div>
</section>

<section class="welcome">
  <div class="welcome-photo" role="img" aria-label="Two women reviewing papers together at a desk"></div>
  <h2>Welcome to Maren Holt Consultancy</h2>
  <p>Lorem Ipsum is simply dummy text of the printing and typesetting industry. Lorem Ipsum has been the industry's standard dummy text ever since the 1500s, when an unknown printer took a galley of type and scrambled it to make a type specimen book.</p>
  <div class="slider-dots"><i class="on"></i><i></i><i></i></div>
</section>

<main class="content">
  <h2 class="section-title">Previous Successful Consultancy</h2>
  <div class="post-divider"></div>
  <div class="posts">
    <article class="post">
      <div class="post-photo" role="img" aria-label="Team gathered around a laptop in a bright office" style="background:linear-gradient(135deg,#e8eef3,#9fb4c6 60%,#4d5d6e)"></div>
      <h3>Lorem Ipsum is simply dummy text</h3>
      <p>There are many variations of passages of Lorem Ipsum available, but the majority have suffered alteration in some form, by injected humour, or randomised words which don't look even slightly believable.</p>
      <a href="#" class="btn-pink">Read More</a><time>October 23, 2016</time>
    </article>
    <article class="post">
      <div class="post-photo" role="img" aria-label="Figure with arms raised against a golden sunset" style="background:radial-gradient(circle at 50% 60%,#ffe59a,#f0a531 40%,#6b3a10)"></div>
      <h3>Lorem Ipsum is simply dummy text</h3>
      <p>There are many variations of passages of Lorem Ipsum available, but the majority have suffered alteration in some form, by injected humour, or randomised words which don't look even slightly believable.</p>
      <a href="#" class="btn-pink">Read More</a><time>October 23, 2016</time>
    </article>
    <article class="post">
      <div class="post-photo" role="img" aria-label="Group celebrating with raised arms under a blue sky" style="background:linear-gradient(180deg,#8fc6ef,#dbe9f4 55%,#2f2f36)"></div>
      <h3>Lorem Ipsum is simply dummy text</h3>
      <p>There are many variations of passages of Lorem Ipsum available, but the majority have suffered alteration in some form, by injected humour, or randomised words which don't look even slightly believable.</p>
      <a href="#" class="btn-pink">Read More</a><time>October 23, 2016</time>
    </article>
    <article class="post">
      <div class="post-photo" role="img" aria-label="Joyful woman with arms outstretched in a glass atrium" style="background:linear-gradient(135deg,#cfe0dc,#8fb0a8 55%,#e9d8e6)"></div>
      <h3>Lorem Ipsum is simply dummy text</h3>
      <p>There are many variations of passages of Lorem Ipsum available, but the majority have suffered alteration in some form, by injected humour, or randomised words which don't look even slightly believable.</p>
      <a href="#" class="btn-pink">Read More</a><time>October 23, 2016</time>
    </article>
    <a href="#" class="view-more" style="top:1050px">View More</a>
  </div>

  <aside class="sidebar">
    <div class="search"><span></span><b>Search</b></div>
    <div class="widget">
      <h4>Subscribe to Blog via Email</h4>
      <p>Enter your email address to subscribe to this blog and receive notifications of new posts by email.</p>
      <div class="field">Enter your E-mail</div>
      <a href="#" class="btn-blue">SUBSCRIBE</a>
    </div>
    <div class="widget">
      <h4>Connect With Me:</h4>
      <div class="connect"><span><i></i>Login with Friendwall</span><span><i></i>Login with deskroster</span></div>
    </div>
    <div class="widget" style="border-bottom:0;padding-bottom:0">
      <h4>Follow me on quillpost</h4>
      <div class="tw-profile">
        <div class="tw-avatar" role="img" aria-label="Profile portrait"></div>
        <strong>Maren Holt</strong><em>@marenholtco</em>
        <small>Mother, wife, accountant, corporate banker &amp; small business fan. Here to help you grow and plan well.</small>
        <span class="tw-follow">Follow</span>
      </div>
      <div class="tweet"><div class="tweet-avatar" role="img" aria-label="Profile portrait"></div><strong>Maren Holt</strong><em>@marenholtco</em><p>Lovely lunch thanks Ana, Beth <b>#lunch #team #friends</b></p><time>14 Oct</time></div>
      <div class="tweet"><div class="tweet-avatar" role="img" aria-label="Profile portrait"></div><strong>Maren Holt</strong><em>@marenholtco</em><p>Lovely lunch thanks Ana, Beth <b>#lunch #team #friends</b></p><time>14 Oct</time></div>
      <div class="tweet"><div class="tweet-avatar" role="img" aria-label="Profile portrait"></div><strong>Maren Holt</strong><em>@marenholtco</em><p>Lovely lunch thanks Ana, Beth <b>#lunch #team #friends</b></p><time>14 Oct</time></div>
      <div class="tw-foot"><span>Embed</span><span>View on quillpost</span></div>
    </div>
  </aside>
</main>

<section class="cards">
  <article class="card">
    <div class="card-photo" role="img" aria-label="Smiling woman in a white blouse" style="background:linear-gradient(180deg,#f4f6f8,#dfe6ec)"></div>
    <h5>Lorem Ipsum dummy text</h5>
    <p>It is a long established fact that a reader will be distracted by the readable content of a page when looking at its layout.</p>
    <a href="#">Read More</a>
  </article>
  <article class="card">
    <div class="card-photo" role="img" aria-label="Many hands giving a thumbs up against the sky" style="background:linear-gradient(180deg,#a9cfe8,#d7b39a)"></div>
    <h5>Lorem Ipsum dummy text</h5>
    <p>It is a long established fact that a reader will be distracted by the readable content of a page when looking at its layout.</p>
    <a href="#">Read More</a>
  </article>
  <article class="card active">
    <div class="card-photo" role="img" aria-label="Woman using a phone in a warm café" style="background:linear-gradient(135deg,#e78fbd,#c8609d 60%,#f0a77a)"></div>
    <h5>Lorem Ipsum dummy text</h5>
    <p>It is a long established fact that a reader will be distracted by the readable content of a page when looking at its layout.</p>
    <a href="#">Read More</a>
  </article>
  <article class="card">
    <div class="card-photo" role="img" aria-label="Smiling woman in front of a bookshelf" style="background:linear-gradient(135deg,#d9c4a6,#8e7a68 60%,#4c4f5e)"></div>
    <h5>Lorem Ipsum dummy text</h5>
    <p>It is a long established fact that a reader will be distracted by the readable content of a page when looking at its layout.</p>
    <a href="#">Read More</a>
  </article>
</section>

<footer class="footer">
  <div class="fcol" style="left:96px">
    <h6>Quick Links</h6>
    <ul><li>Home</li><li>Blo</li><li>Services</li><li>News</li><li>Contact Us</li></ul>
  </div>
  <div class="fcol" style="left:306px">
    <h6>Contact Us</h6>
    <div class="who">Maren Holt</div>
    <div class="lines">T: 800-555-0147, ext. 2210<br>E: info@marenholt.com</div>
  </div>
  <div class="fcol" style="left:590px">
    <h6>Quick Message</h6>
    <p class="intro">Lorem Ipsum is simply dummy text of the industry.</p>
    <div class="ffield">Email</div>
    <div class="ffield tall">Message</div>
    <span class="fsend">SEND</span>
  </div>
  <div class="fcol" style="left:889px">
    <h6>Social Media</h6>
    <div class="socials"><span>quill</span><span>desk</span><span>wall</span><span>circle</span></div>
  </div>
</footer>
<div class="copyright">Copyrights 2016 MarenHolt.All Rights Reserved</div>

</body>
</html>
```